Australian Training Organisation Needs a Flyer for Tourism Training

I am an Australian Registered Training Organisation and have flyers that I would like to have designed. We deliver training to our local market in Tourism Hospitality and Events. You can see some examples of other brochures we have designed at http://www.kelvoramesh.com.au/bus-admin-management.html I would like something that is very modern, two sided and visual. I have added information about the training - a couple of very important things to note: All the information must be on the flyer, including codes of course. The two logos must be on the flyer (the upside down triangle logo must be next to the name Cert II in Tourism. The wording, KL Drovemark Pty Ltd (RTO 48167) must be on the flyer (can be down bottom in small text). We also have a promotion - a FREE 2 day barista course for every enrolment. I have another 3 flyers in same format to do for the successful designer.

Target Market(s)

Gen Y - Z

Industry/Entity Type

Tourism

Requirements
Must have
• Both logos
• KL Drovemark Pty Ltd (RTO 48167)
• All course codes
• All the information that is on the attached brief
Nice to have
• Very visual, without being too busy
• pictures of happy students

```html
<!DOCTYPE html>
<html lang="en">
<head>
<meta charset="utf-8">
<title>KL Drovemark – Course Flyer</title>
<link href="https://fonts.googleapis.com/css2?family=Roboto:wght@300;400;500&display=swap" rel="stylesheet">
<style>
  :root{
    --red:#e8334a;
    --yellow:#f2f08e;
    --paper:#f3f3f3;
    --ink:#1c1c1c;
    --white:#ffffff;
    --brown:#5b2a1f;
    --mint:#d9ece2;
  }
  *{margin:0;padding:0;box-sizing:border-box}
  html,body{width:849px;height:1200px;overflow:hidden;background:var(--paper)}
  body{font-family:"Roboto",Arial,sans-serif;color:var(--ink);font-weight:300}
  .flyer{position:relative;width:849px;height:1200px;overflow:hidden;background:var(--paper)}
  .shapes{position:absolute;inset:0;width:849px;height:1200px}

  .tab{position:absolute;left:0;background:var(--red);color:var(--white);box-shadow:0 10px 10px -6px rgba(0,0,0,.45)}
  .tab--duration{top:273px;width:328px;height:52px;padding:0 0 0 55px;font-size:17px;font-weight:400;line-height:52px;letter-spacing:.1px}
  .tab--promo{left:353px;top:835px;width:237px;height:46px;text-align:center;font-size:28px;font-weight:400;line-height:46px}

  .duration-text{position:absolute;left:55px;top:344px;width:748px;font-size:16px;line-height:28px;letter-spacing:-.1px}
  .duration-text .line{display:block;white-space:nowrap;text-align:justify;text-align-last:justify}
  .duration-text .line--end{text-align-last:left}

  .heading{position:absolute;left:55px;font-size:29px;font-weight:400}
  .heading--fees{top:568px}
  .heading--dates{top:831px}
  .fees{position:absolute;left:55px;top:603px;font-size:16.5px;line-height:28px;white-space:nowrap}
  .fees .price{color:var(--red)}
  .dates{position:absolute;left:55px;top:869px;font-size:16.5px}

  .promo-badge{position:absolute;left:571px;top:646px;width:314px;height:314px;border-radius:50%;background:var(--yellow)}
  .promo-badge__inner{position:absolute;left:16px;top:14px;width:288px;height:288px;border-radius:50%;background:var(--white);box-shadow:inset 16px 4px 18px -8px rgba(0,0,0,.4)}
  .promo-text{position:absolute;left:611px;top:706px;width:260px;text-align:center;font-weight:400}
  .promo-text__lead{font-size:25px;line-height:26px;font-weight:500}
  .promo-text__codes{margin-top:18px;font-size:29px;line-height:34px}

  .contact{position:absolute;left:22px;top:1036px;color:var(--white);font-size:20px;line-height:28.5px}
  .contact li{list-style:none;display:flex;align-items:center}
  .contact svg{width:22px;height:22px;margin-right:11px;flex:none}

  .brand{position:absolute;left:575px;top:1094px;width:243px;height:62px;background:var(--brown);display:flex;align-items:center;justify-content:center;gap:9px}
  .brand__mark{width:14px;height:14px;background:var(--red)}
  .brand__name{color:var(--red);font-size:22px;font-weight:500}
  .rto-line{position:absolute;left:22px;top:1169px;color:var(--white);font-size:17.2px;white-space:nowrap}
</style>
</head>
<body>
<main class="flyer">
  <svg class="shapes" viewBox="0 0 1058 1496" preserveAspectRatio="none">
    <defs>
      <linearGradient id="photoTone" x1="0" y1="0" x2="1" y2="1">
        <stop offset="0" stop-color="#9fb07e"/>
        <stop offset=".5" stop-color="#d9b9a4"/>
        <stop offset="1" stop-color="#eae6c8"/>
      </linearGradient>
    </defs>
    <polygon role="img" aria-label="Photo of smiling school children sitting in a row" fill="url(#photoTone)" points="0,0 1058,0 1058,112 570,322 0,112"/>
    <polygon fill="var(--yellow)" points="1058,112 570,322 570,332 1058,132"/>
    <polygon fill="var(--red)" points="0,112 570,322 570,332 0,228"/>
    <polygon fill="#d8d8d8" points="0,228 570,332 580,340 0,238" opacity=".6"/>
    <polygon fill="var(--yellow)" points="0,1215 800,1235 800,1252 0,1252"/>
    <polygon fill="var(--red)" points="0,1250 795,1250 720,1322 1058,1290 1058,1496 0,1496"/>
    <polygon fill="var(--mint)" points="740,1300 1058,1278 1058,1292 720,1322"/>
  </svg>

  <div class="tab tab--duration">DURATION OF THE COURSE</div>
  <p class="duration-text">
    <span class="line">2 Days per week x 24 weeks at KL Drovemark Pty Ltd Tallowbrook Campus and 1 week industry placement.</span>
    <span class="line">Face to face training is completed during classroom time and students are required to complete some</span>
    <span class="line line--end">out of the class assessments.</span>
    <span class="line">The course is delivered through our dynamic and interactive learning portal and it is recommended that</span>
    <span class="line">student have access to reliable internet connection at home. Student Support Hub is located at 18</span>
    <span class="line">Calder Street for student’s convenience. Online learning option – student are recommended to complete</span>
    <span class="line line--end">a minimum of 20 hours per week to complete the course within a 6 month time frame.</span>
  </p>

  <h2 class="heading heading--fees">Fees:</h2>
  <div class="fees">
    <p>This course is covered by Queensland VET Investment Plan under the Certificate III Guarantee program.</p>
    <p>If eligible the following prices apply:</p>
    <p class="price">Cert III Guarantee Concession $1245.00</p>
    <p class="price">Cert III Guarantee Non Concession $1565.00</p>
    <p class="price">VET in Schools (open to school students) $132.00</p>
    <p class="price">Full price (no subsidy available) $2845.00</p>
    <p>Flexible Payment Plans are available</p>
  </div>

  <h2 class="heading heading--dates">Course Dates:</h2>
  <p class="dates">Course starts 18/07/2016</p>

  <div class="promo-badge"><div class="promo-badge__inner"></div></div>
  <div class="tab tab--promo">PROMOTION</div>
  <div class="promo-text">
    <p class="promo-text__lead">Enrol today to<br>receive a FREE<br>Barista Course</p>
    <p class="promo-text__codes">SITHFAB012A<br>and<br>SITHFAB016A</p>
  </div>

  <ul class="contact">
    <li><svg viewBox="0 0 24 24"><rect x="6" y="1" width="12" height="22" rx="2" fill="none" stroke="#fff" stroke-width="2"/><rect x="8" y="4" width="8" height="13" fill="#fff"/></svg>(07) 4158 2906</li>
    <li><svg viewBox="0 0 24 24" fill="none" stroke="#fff" stroke-width="1.8"><circle cx="12" cy="12" r="9"/><ellipse cx="12" cy="12" rx="4" ry="9"/><line x1="3" y1="12" x2="21" y2="12"/><line x1="5" y1="7" x2="19" y2="7"/><line x1="5" y1="17" x2="19" y2="17"/></svg>www.kelvoramesh.com.au</li>
    <li><svg viewBox="0 0 24 24"><rect x="1" y="5" width="22" height="14" fill="#fff"/></svg>learn.it@kelvoramesh.com.au</li>
    <li>18 Calder Street TALLOWBROOK QLD 4872</li>
  </ul>

  <div class="brand"><span class="brand__mark"></span><span class="brand__name">KL Drovemark</span></div>

  <p class="rto-line">KL Drovemark Pty Ltd is a Tallowbrook Coast Owned and Operated Registered Training Organisation 48167</p>
</main>
</body>
</html>
```